Mirela Causo Photography

I need a website design for my photography business, I want something clean, elegant, Classy.. I like the colors, White, Black, Green/Blue, Pink, Brown, Lavender,, I have a lot added my Logo .... Additional Info... I need a Photography Website Design, with probably 6 Tabs, Home, About Me, Portfolio, Gallery, Investment, Contact.
Home Page should have my logo, Name & Address, Social Media Icons, and Pictures.
As long as the templates are made I have a hosting coming that will code it.
Target Market(s)
Portraits Photography, Senior Portraits, Newborn, Families, Events, Engagements, Wedding,
Industry/Entity Type
Business
Number of Pages Required
5+ page
Look and feel

```html
<!DOCTYPE html>
<html lang="en">
<head>
<meta charset="utf-8">
<title>Mirela Causo Photography</title>
<link href="https://fonts.googleapis.com/css2?family=Raleway:wght@300;400;500&family=Open+Sans:wght@400;600&display=swap" rel="stylesheet">
<style>
  :root {
    --ink: #222220;
    --charcoal: #2b2b29;
    --contact-bar: #262624;
    --footer: #3d3d35;
    --white: #ffffff;
    --muted: #b9b9b0;
    --green: #6fd12e;
    --pink: #e7a3cf;
    --lavender: #dcaeda;
    --lavender-ink: #4a3446;
    --nav-active: #3a3a38;
  }
  * { box-sizing: border-box; margin: 0; padding: 0; }
  html, body { width: 831px; height: 1200px; overflow: hidden; background: var(--white); }
  body { position: relative; font-family: "Open Sans", Arial, sans-serif; color: var(--ink); }
  .abs { position: absolute; }

  /* hero */
  .hero { left: 0; top: 0; width: 831px; height: 413px;
    background:
      radial-gradient(circle at 88% 30%, rgba(255,244,200,.95) 0%, rgba(255,214,140,.55) 9%, rgba(255,190,120,0) 28%),
      radial-gradient(ellipse 60% 18% at 30% 34%, rgba(90,60,90,.55) 0%, rgba(90,60,90,0) 100%),
      radial-gradient(ellipse 40% 16% at 80% 44%, rgba(40,55,45,.6) 0%, rgba(40,55,45,0) 100%),
      radial-gradient(ellipse 30% 14% at 50% 92%, rgba(200,90,50,.75) 0%, rgba(200,90,50,0) 100%),
      radial-gradient(ellipse 22% 14% at 82% 90%, rgba(190,50,50,.7) 0%, rgba(190,50,50,0) 100%),
      radial-gradient(ellipse 20% 12% at 20% 96%, rgba(210,110,60,.7) 0%, rgba(210,110,60,0) 100%),
      linear-gradient(180deg, #7f86aa 0%, #b7a6a8 12%, #e2c39a 24%, #8d6a78 32%, #6b5a6a 40%, #4d6b5e 48%, #6aa8a0 58%, #9fc6a8 68%, #d9d39a 80%, #c49a62 92%, #8a5a3a 100%); }
  .top-bar { left: 0; top: 0; width: 831px; height: 20px; background: rgba(40,40,60,.4);
    font-size: 6.5px; color: var(--white); }
  .top-contact { left: 168px; top: 6px; letter-spacing: .2px; }
  .top-contact span { margin: 0 7px; }
  .top-social { left: 604px; top: 6px; display: flex; gap: 6px; }
  .social-chip { width: 8px; height: 8px; border: 1px solid var(--white); border-radius: 2px; }

  .brand { left: 172px; top: 40px; width: 132px; display: flex; flex-direction: column; align-items: center; gap: 6px; }
  .brand-mark { width: 30px; height: 30px; border-radius: 50%; background: var(--ink); }
  .brand-name { font-family: "Raleway", Arial, sans-serif; font-weight: 400; font-size: 15px;
    line-height: 1.15; color: var(--ink); text-align: center; }

  .main-nav { left: 411px; top: 76px; display: flex; gap: 4px; font-size: 7.5px; color: var(--ink); }
  .main-nav a { color: inherit; text-decoration: none; padding: 5px 7px; border-radius: 2px; }
  .main-nav a.is-active { background: var(--nav-active); color: var(--white); }

  .slide-band { left: 0; top: 178px; width: 831px; height: 77px; background: rgba(50,40,50,.3); }
  .slide-title { left: 0; top: 194px; width: 831px; text-align: center;
    font-family: "Raleway", Arial, sans-serif; font-weight: 300; font-size: 39px;
    letter-spacing: 1px; color: var(--white); }
  .arrow { top: 199px; }

  /* intro */
  .intro { left: 0; top: 416px; width: 831px; height: 165px;
    background:
      radial-gradient(ellipse 9% 30% at 23% 105%, rgba(120,110,95,.6) 0%, rgba(120,110,95,0) 100%),
      radial-gradient(ellipse 12% 38% at 50% 100%, rgba(135,125,110,.6) 0%, rgba(135,125,110,0) 100%),
      radial-gradient(ellipse 10% 30% at 75% 105%, rgba(120,110,95,.55) 0%, rgba(120,110,95,0) 100%),
      linear-gradient(180deg, #2a2a28 0%, #2e2d2b 60%, #3a3834 100%); }
  .intro-box { left: 264px; top: 465px; width: 303px; height: 69px; border: 1px solid var(--green);
    text-align: center; color: var(--white); }
  .intro-kicker { font-family: "Raleway", Arial, sans-serif; font-size: 10.5px; margin-top: 7px; letter-spacing: .3px; }
  .intro-title { font-family: "Raleway", Arial, sans-serif; font-weight: 300; font-size: 27px; line-height: 1.05; }
  .intro-text { font-size: 7px; }
  .pager { left: 368px; top: 560px; display: flex; }
  .pager i { width: 32px; height: 5px; border: 1px solid #8fa5a5; }
  .pager i.is-current { background: var(--green); border-color: var(--green); }

  /* portfolio */
  .portfolio-band { left: 0; top: 581px; width: 831px; height: 46px; background: var(--lavender); }
  .portfolio-title { left: 0; top: 589px; width: 831px; text-align: center;
    font-family: "Raleway", Arial, sans-serif; font-weight: 400; font-size: 26px;
    letter-spacing: 1.5px; color: var(--lavender-ink); }
  .tile { height: 190px; display: flex; align-items: center; justify-content: center; }
  .tile-label { font-family: "Raleway", Arial, sans-serif; font-size: 13.5px; color: var(--white); letter-spacing: .3px; }
  .tile.is-hover .tile-label { color: var(--green); }
  .tile-frame { left: 294px; top: 662px; width: 233px; height: 141px;
    border-top: 1px solid var(--green); border-right: 1px solid var(--green); }
  .tile-frame-b { left: 294px; top: 650px; width: 226px; height: 139px;
    border-left: 1px solid var(--green); border-bottom: 1px solid var(--green); }

  /* contact strip */
  .contact-bar { left: 0; top: 1007px; width: 831px; height: 55px; background: var(--contact-bar); }
  .contact-line { left: 184px; top: 1026px; color: var(--white);
    font-family: "Raleway", Arial, sans-serif; font-size: 14px; font-weight: 500; }
  .contact-line small { font-family: "Open Sans", Arial, sans-serif; font-size: 7px; font-weight: 400; }
  .btn-contact { left: 524px; top: 1022px; width: 125px; height: 25px; background: var(--pink);
    color: var(--ink); font-family: "Raleway", Arial, sans-serif; font-size: 11px;
    display: flex; align-items: center; justify-content: center; letter-spacing: .4px; }

  /* follow */
  .follow-note { left: 0; top: 1077px; width: 831px; text-align: center; font-size: 7.5px; }
  .btn-follow { left: 352px; top: 1101px; width: 126px; height: 25px; border: 1px solid var(--ink);
    font-family: "Raleway", Arial, sans-serif; font-size: 11px; letter-spacing: .4px;
    display: flex; align-items: center; justify-content: center; }
  .follow-social { left: 374px; top: 1136px; display: flex; gap: 9px; }
  .follow-social .social-chip { width: 11px; height: 11px; border: 1.5px solid var(--ink); }

  .site-footer { left: 0; top: 1163px; width: 831px; height: 37px; background: var(--footer);
    color: var(--muted); font-size: 6.5px; display: flex; align-items: center; justify-content: center; }
</style>
</head>
<body>
  <header>
    <div class="abs hero" role="img" aria-label="Mountain lake at sunset with red rowing boats moored in the foreground"></div>
    <div class="abs top-bar">
      <div class="abs top-contact">&#9742; 555.0147.2290<span>|</span>&#9993; info@mirelacausophotography.com</div>
      <div class="abs top-social" aria-label="Social media links"><i class="social-chip"></i><i class="social-chip"></i><i class="social-chip"></i><i class="social-chip"></i><i class="social-chip"></i></div>
    </div>
    <div class="abs brand">
      <span class="brand-mark"></span>
      <span class="brand-name">Mirela Causo<br>Photography</span>
    </div>
    <nav class="abs main-nav">
      <a class="is-active">Home</a><a>About Me</a><a>Portfolio</a><a>Gallery</a><a>Investment</a><a>Contact</a>
    </nav>
    <div class="abs slide-band"></div>
    <h1 class="abs slide-title">EXCELLENT SOLUTION</h1>
    <svg class="abs arrow" style="left:91px" width="34" height="34" viewBox="0 0 34 34" aria-label="Previous slide">
      <circle cx="17" cy="17" r="16" fill="none" stroke="#fff" stroke-width="1.6"/>
      <polyline points="20,9 12,17 20,25" fill="none" stroke="#fff" stroke-width="1.6"/>
    </svg>
    <svg class="abs arrow" style="left:692px" width="34" height="34" viewBox="0 0 34 34" aria-label="Next slide">
      <circle cx="17" cy="17" r="16" fill="none" stroke="rgba(255,255,255,.45)" stroke-width="1.6"/>
      <polyline points="14,9 22,17 14,25" fill="none" stroke="rgba(255,255,255,.45)" stroke-width="1.6"/>
    </svg>
  </header>

  <section>
    <div class="abs intro" role="img" aria-label="Close-up of vintage camera lenses on a dark surface"></div>
    <div class="abs intro-box">
      <p class="intro-kicker">CAPTURE THE MOMENT</p>
      <h2 class="intro-title">PHOTO</h2>
      <p class="intro-text">Quality photography that preserves treasured memories.</p>
    </div>
    <div class="abs pager"><i class="is-current"></i><i></i><i></i></div>
  </section>

  <section>
    <div class="abs portfolio-band"></div>
    <h2 class="abs portfolio-title">PORTFOLIO</h2>

    <div class="abs tile" style="left:0;top:627px;width:261px;background:radial-gradient(ellipse 40% 40% at 50% 45%,rgba(130,110,85,.55),rgba(130,110,85,0)),linear-gradient(180deg,#2d2a24 0%,#4a4236 45%,#5a5248 70%,#3a352f 100%)" role="img" aria-label="Couple playing with a shopping cart in an empty car park"><span class="tile-label">SAMPLE IMAGE - CATEGORY 1</span></div>
    <div class="abs tile is-hover" style="left:261px;top:627px;width:284px;background:radial-gradient(ellipse 35% 45% at 60% 40%,rgba(150,120,105,.6),rgba(150,120,105,0)),linear-gradient(160deg,#5a504a 0%,#3c3532 50%,#222020 100%)" role="img" aria-label="Fashion portrait of a woman wearing jewellery"><span class="tile-label">SAMPLE IMAGE - CATEGORY 1</span></div>
    <div class="abs tile" style="left:545px;top:627px;width:286px;background:radial-gradient(ellipse 45% 30% at 60% 25%,rgba(80,110,60,.6),rgba(80,110,60,0)),radial-gradient(ellipse 50% 25% at 55% 88%,rgba(40,80,85,.7),rgba(40,80,85,0)),linear-gradient(180deg,#2c3626 0%,#262a22 55%,#1d2a2c 100%)" role="img" aria-label="Woman lying on the bonnet of a vintage car under palm trees"><span class="tile-label">SAMPLE IMAGE - CATEGORY 1</span></div>
    <div class="abs tile" style="left:0;top:817px;width:261px;background:radial-gradient(circle at 40% 22%,rgba(220,170,90,.55),rgba(220,170,90,0) 22%),linear-gradient(180deg,#26343a 0%,#2a3840 50%,#1c2428 100%)" role="img" aria-label="Hands holding a lit sparkler"><span class="tile-label">SAMPLE IMAGE - CATEGORY 1</span></div>
    <div class="abs tile" style="left:261px;top:817px;width:284px;background:radial-gradient(ellipse 35% 40% at 55% 70%,rgba(150,100,70,.6),rgba(150,100,70,0)),radial-gradient(ellipse 30% 20% at 40% 15%,rgba(170,120,80,.55),rgba(170,120,80,0)),linear-gradient(180deg,#6c6c48 0%,#5e5a3c 60%,#4a4030 100%)" role="img" aria-label="Child in aviator goggles holding a wooden toy plane"><span class="tile-label">SAMPLE IMAGE - CATEGORY 1</span></div>
    <div class="abs tile" style="left:545px;top:817px;width:286px;background:linear-gradient(180deg,#4d6580 0%,#5a6f86 40%,#8c98a8 58%,#3a4a60 72%,#232e40 100%)" role="img" aria-label="Paraglider above snowy mountains"><span class="tile-label">SAMPLE IMAGE - CATEGORY 1</span></div>
    <div class="abs tile-frame"></div>
    <div class="abs tile-frame-b"></div>
  </section>

  <section>
    <div class="abs contact-bar"></div>
    <p class="abs contact-line">WANT TO CONTACT, <small>just click on the contact button at the right</small></p>
    <a class="abs btn-contact">CONTACT ME</a>
  </section>

  <section>
    <p class="abs follow-note">To get the latest update of me and my works</p>
    <a class="abs btn-follow">FOLLOW ME</a>
    <div class="abs follow-social" aria-label="Social media links"><i class="social-chip"></i><i class="social-chip"></i><i class="social-chip"></i><i class="social-chip"></i><i class="social-chip"></i></div>
  </section>

  <footer class="abs site-footer">© 2015, All Rights Reserved.</footer>
</body>
</html>
```